Label design for our new range of organic honey.

We need a design for honey jars and tubs. The label needs to indicate we are located in the Western Australia. The design needs to be elegant, modern and attracting high end customers that focus on quality.

Need extra days to review

```html
<!DOCTYPE html>
<html lang="en">
<head>
<meta charset="utf-8">
<title>Organic Honey Label</title>
<link rel="stylesheet" href="https://fonts.googleapis.com/css2?family=Source+Serif+4:ital,opsz,wght@0,8..60,400;0,8..60,500;1,8..60,400&display=swap">
<style>
  :root {
    --page-bg: #f7f7f7;
    --label-dark: #3a3a3a;
    --label-mid: #4a4a4a;
    --text-light: #ffffff;
    --gold-deep: #8a7a45;
    --gold-mid: #c9b36e;
    --gold-light: #f1e3a6;
  }
  html, body {
    margin: 0;
    padding: 0;
    width: 1200px;
    height: 1200px;
    overflow: hidden;
    background: var(--page-bg);
  }
  .label {
    display: block;
    width: 1200px;
    height: 1200px;
  }
  .label-text {
    font-family: "Source Serif 4", Georgia, serif;
  }
  .label-organic {
    fill: var(--text-light);
    font-size: 70px;
    font-weight: 500;
  }
  .label-product {
    font-size: 136px;
    font-weight: 400;
    letter-spacing: 2px;
  }
  .label-purity {
    fill: var(--text-light);
    font-size: 45px;
    font-weight: 400;
  }
  .label-origin {
    fill: var(--text-light);
    font-size: 34px;
    font-style: italic;
  }
  .brand-name {
    fill: var(--text-light);
    font-size: 25px;
    font-weight: 400;
    letter-spacing: 4px;
  }
  .brand-dot {
    fill: none;
    stroke: var(--text-light);
    stroke-width: 2;
  }
</style>
</head>
<body>
<svg class="label" viewBox="0 0 1200 1200" xmlns="http://www.w3.org/2000/svg">
  <defs>
    <linearGradient id="label-surface" x1="0" y1="1" x2="1" y2="0">
      <stop offset="0" stop-color="var(--label-dark)"/>
      <stop offset="1" stop-color="var(--label-mid)"/>
    </linearGradient>
    <linearGradient id="gold-foil" x1="0" y1="0" x2="1" y2="0">
      <stop offset="0" stop-color="var(--gold-deep)"/>
      <stop offset="0.55" stop-color="var(--gold-light)"/>
      <stop offset="1" stop-color="var(--gold-mid)"/>
    </linearGradient>
    <radialGradient id="map-tone" cx="0.55" cy="0.45" r="0.6">
      <stop offset="0" stop-color="#555555" stop-opacity="0.55"/>
      <stop offset="1" stop-color="#3a3a3a" stop-opacity="0"/>
    </radialGradient>
    <clipPath id="label-shape">
      <polygon points="60,600 330,127 870,127 1140,600 870,1073 330,1073"/>
    </clipPath>
  </defs>

  <!-- hexagonal label -->
  <polygon class="label-body" points="84,600 342,148 858,148 1116,600 858,1052 342,1052"
           fill="url(#label-surface)" stroke="url(#label-surface)" stroke-width="44" stroke-linejoin="round"/>

  <!-- map of Australia area -->
  <g clip-path="url(#label-shape)">
    <rect role="img" aria-label="Outline map of Australia" x="80" y="160" width="1060" height="900" fill="url(#map-tone)"/>
  </g>

  <!-- brand mark area -->
  <g class="brand">
    <circle class="brand-dot" cx="328" cy="548" r="14"/>
    <text class="label-text brand-name" x="328" y="600" text-anchor="middle">REDGUM RIDGE</text>
    <text class="label-text brand-name" x="328" y="636" text-anchor="middle">HONEY</text>
  </g>

  <!-- product text -->
  <text class="label-text label-organic" x="758" y="496" text-anchor="middle">organic</text>
  <text class="label-text label-product" x="748" y="634" text-anchor="middle" fill="url(#gold-foil)">HONEY</text>
  <text class="label-text label-purity" x="758" y="700" text-anchor="middle">100% Pure</text>

  <text class="label-text label-origin" x="504" y="847">from</text>
  <text class="label-text label-origin" x="411" y="889">Western Australia</text>

  <rect class="gold-bar" x="392" y="920" width="327" height="19" fill="url(#gold-foil)"/>
</svg>
</body>
</html>
```